the halvorsen group premier division

design a DL A4 tri fold brochure to reflect our creative landscape business
my web site www.thehalvorsengroup.com.au
has all the information needed
i will also be updating the website to be more updated and creative design

```html
<!DOCTYPE html>
<html lang="en">
<head>
<meta charset="utf-8">
<title>The Halvorsen Group – Tri-fold Brochure</title>
<link href="https://fonts.googleapis.com/css2?family=Montserrat:wght@400;500;600;700&display=swap" rel="stylesheet">
<style>
:root{
  --green:#6cbb3c;
  --green-dark:#4f9a2a;
  --orange:#f28c28;
  --blue:#3aa0dc;
  --ink:#2b2b2b;
  --grey:#555;
  --paper:#ffffff;
  --bg:#e9e9e9;
}
*{box-sizing:border-box;margin:0;padding:0}
html,body{width:800px;height:1200px;overflow:hidden;background:var(--bg);font-family:'Montserrat',sans-serif;color:var(--ink)}
.spread{position:absolute;left:30px;width:740px;height:523px;display:flex;box-shadow:0 6px 20px rgba(0,0,0,.18)}
.spread--outside{top:40px}
.spread--inside{top:626px}
.panel{position:relative;width:246.67px;height:100%;background:var(--paper);overflow:hidden}
.panel+.panel{border-left:1px solid #e4e4e4}
.photo{position:absolute;border-radius:50%;border:2px solid #fff;box-shadow:0 0 0 1px var(--blue)}
.dot{position:absolute;border-radius:50%;opacity:.85}
.dot--orange{background:var(--orange)}
.dot--green{background:var(--green)}
.dot--blue{background:var(--blue)}
h2{font-weight:500;font-size:15px;letter-spacing:.5px;text-transform:uppercase}
h2 b{color:var(--green);font-weight:700}
h3{color:var(--orange);font-weight:600;font-size:11.5px;margin:10px 0 4px}
p{font-size:7.2px;line-height:1.45;color:var(--grey);margin-bottom:6px}
.about-copy{position:absolute;left:22px;right:20px;top:212px}
.about-copy h2{margin-bottom:10px}
/* back panel */
.back-band{position:absolute;left:0;top:0;width:100%;height:150px;background:var(--green)}
.show-badge{position:absolute;left:73px;top:272px;width:100px;height:34px;border:1px solid var(--orange);border-radius:2px;background:#fff}
.show-note{position:absolute;left:20px;right:20px;top:312px;text-align:center;font-size:6.5px;line-height:1.4;color:var(--grey)}
.contact-name{position:absolute;left:16px;right:16px;top:346px;text-align:center;color:var(--green-dark);font-weight:600;font-size:10.5px;line-height:1.35}
.rule{width:22px;height:2px;background:var(--orange);margin:6px auto 0}
.contact-list{position:absolute;left:28px;top:398px;list-style:none;font-size:9px;line-height:2.05}
.contact-list li{display:flex;align-items:center;gap:7px}
.contact-list svg{width:9px;height:9px;flex:none}
/* cover */
.brand{position:absolute;left:0;right:0;top:22px;text-align:center}
.brand-mark{width:24px;height:24px;border-radius:50%;background:var(--orange);margin:0 auto 6px}
.brand-name{font-weight:700;font-size:16px;color:var(--ink)}
.brand-sub{font-weight:500;font-size:6.5px;letter-spacing:2.6px;text-transform:uppercase;color:var(--grey);margin-top:2px}
.cover-band{position:absolute;left:0;bottom:0;width:100%;height:175px;background:var(--green)}
.tagline{position:absolute;left:0;right:0;bottom:78px;text-align:center;color:#fff;font-size:14px;letter-spacing:.5px;line-height:1.25}
.tagline strong{display:block;font-weight:700;font-size:16px}
.tagline .rule{background:#fff;margin-top:8px}
.url-bar{position:absolute;left:24px;right:24px;bottom:34px;height:22px;background:var(--orange);color:#fff;font-size:8.5px;font-weight:500;display:flex;align-items:center;justify-content:center}
/* inside */
.services-copy{position:absolute;left:22px;right:18px;top:26px}
.inst-copy{position:absolute;left:18px;right:18px;top:130px}
.checks{display:flex;gap:14px;margin:4px 0 6px}
.checks ul{list-style:none;font-size:7.2px;line-height:1.5;color:var(--ink)}
.checks li::before,.consult li::before{content:"✓";color:var(--blue);font-weight:700;margin-right:4px}
.consult{position:absolute;left:22px;right:14px;top:150px}
.consult h2{font-size:13.5px;line-height:1.25}
.consult h3{margin:9px 0 2px;font-size:10.5px}
.consult ul{list-style:none;font-size:8.6px;line-height:1.55}
.grass{position:absolute;left:0;bottom:0;width:100%;height:70px;background:linear-gradient(180deg,rgba(110,190,50,0) 0%,#8ccf3f 55%,#5fa52a 100%)}
</style>
</head>
<body>

<section class="spread spread--outside">
  <article class="panel panel--about">
    <div class="photo" role="img" aria-label="Stone garden path lined with lush tropical plants" style="left:10px;top:-90px;width:230px;height:230px;background:radial-gradient(circle at 45% 65%,#c9c2b3 0%,#a8b58a 40%,#4e7d37 75%,#2f5a25 100%)"></div>
    <div class="dot dot--orange" style="left:32px;top:120px;width:40px;height:40px"></div>
    <div class="about-copy">
      <h2>About <b>Us</b></h2>
      <p>The Halvorsen Group (THG), formerly Lindqvist Landscapes, is a professional landscaping and construction service that takes pride in delivering high-end outdoor landscapes across Melbourne, Victoria.</p>
      <p>Erik Lindqvist, head of The Halvorsen Group, offers a team that dedicates their efforts from concept development to installation and maintenance to ensure the outdoor creation becomes part of the client's home and life experience with visual, tactile and sensory inclusions.</p>
      <p>Over its 20 years, the business has developed a strong reputation for positive customer experiences, innovative designs and quality outcomes to suit individual needs and design styles. When working with Erik Lindqvist's team, you work with a qualified ensemble of experienced landscapers and horticulturalists.</p>
      <p>At The Halvorsen Group, we'll endeavour to uphold our high level of professionalism and excellence in the residential and large property markets including inner suburban settings through to acreage of various climates.</p>
    </div>
  </article>

  <article class="panel panel--back">
    <div class="back-band"></div>
    <div class="photo" role="img" aria-label="Outdoor lounge terrace overlooking a harbour" style="left:33px;top:70px;width:180px;height:180px;background:linear-gradient(180deg,#cfe3f2 0%,#b9cfe0 38%,#8a7b5c 55%,#c9a877 75%,#6d5636 100%)"></div>
    <div class="dot dot--orange" style="left:100px;top:46px;width:46px;height:46px"></div>
    <div class="show-badge" aria-hidden="true"></div>
    <div class="show-note">Visit us at Stand B12<br>Fri 8 – Sun 10 March<br>Riverside Exhibition Hall</div>
    <div class="contact-name">Erik Lindqvist The Halvorsen Group –<br>Premier Division<div class="rule"></div></div>
    <ul class="contact-list">
      <li><svg viewBox="0 0 10 10"><path d="M5 0a3.5 3.5 0 0 0-3.5 3.5C1.5 6 5 10 5 10s3.5-4 3.5-6.5A3.5 3.5 0 0 0 5 0zm0 5a1.5 1.5 0 1 1 0-3 1.5 1.5 0 0 1 0 3z" fill="#f28c28"/></svg>PO Box 742 Kingsford VIC 3090</li>
      <li><svg viewBox="0 0 10 10"><path d="M2 0.5l2 2-1 1.3a6 6 0 0 0 3.2 3.2l1.3-1 2 2-1.2 1.5C4.5 9.5 0.5 5.5 0.5 1.7z" fill="#f28c28"/></svg>0400 123 987</li>
      <li><svg viewBox="0 0 10 10"><rect x="0.5" y="2" width="9" height="6" fill="#f28c28"/><path d="M0.5 2l4.5 3.5L9.5 2" stroke="#fff" fill="none"/></svg>info@thehalvorsengroup.com.au</li>
      <li><svg viewBox="0 0 10 10"><circle cx="5" cy="5" r="4.5" fill="#f28c28"/><path d="M0.5 5h9M5 0.5c-2.5 3-2.5 6 0 9M5 0.5c2.5 3 2.5 6 0 9" stroke="#fff" stroke-width=".7" fill="none"/></svg>www.thehalvorsengroup.com.au</li>
    </ul>
  </article>

  <article class="panel panel--cover">
    <div class="brand">
      <div class="brand-mark"></div>
      <div class="brand-name">The Halvorsen Group</div>
      <div class="brand-sub">Premier Division</div>
    </div>
    <div class="cover-band"></div>
    <div class="photo" role="img" aria-label="Paved courtyard with outdoor seating among shrubs" style="left:-40px;top:138px;width:140px;height:140px;background:radial-gradient(circle at 60% 55%,#9a9a9a 0%,#6f7a63 45%,#3d5a2c 100%)"></div>
    <div class="photo" role="img" aria-label="Lush garden with colourful shrubs and lawn" style="left:88px;top:128px;width:165px;height:165px;background:radial-gradient(circle at 50% 50%,#c8d64a 0%,#8dbb35 45%,#3f7a22 100%)"></div>
    <div class="photo" role="img" aria-label="Stepping stone path across a green lawn" style="left:40px;top:222px;width:120px;height:120px;background:linear-gradient(160deg,#5b8c34 0%,#7fae45 45%,#8a8f85 60%,#4e7a2b 100%)"></div>
    <div class="dot dot--orange" style="left:150px;top:110px;width:40px;height:40px"></div>
    <div class="tagline">Landscaping to<strong>Your Lifestyle</strong><div class="rule"></div></div>
    <div class="url-bar">www.thehalvorsengroup.com.au</div>
  </article>
</section>

<section class="spread spread--inside">
  <article class="panel panel--services">
    <div class="services-copy">
      <h2>Our <b>Services</b></h2>
      <h3>Consultation and Design</h3>
      <p>The Halvorsen Group can work with you for a full landscape design concept or visit your site to discuss an existing plan.</p>
      <p>Our landscape designers will begin by discussing your needs and look at your property and setting to create a concept where all attributes are considered from the land itself, design style, the elements and impact, through to lifestyle, and functionality and of course budget.</p>
      <h3>Earthwork &amp; Site Preparation</h3>
      <p>Depending on the nature of the site, it is imperative that your foundation and earth is well prepared for construction and planting. This will determine a quality outcome and the longevity we promote so you don't have issues in the future.</p>
    </div>
    <div class="photo" role="img" aria-label="Rooftop terrace with glass table overlooking a city bridge" style="left:-20px;top:352px;width:300px;height:300px;background:linear-gradient(180deg,#d6e8f3 0%,#b7cddb 20%,#7fae4a 32%,#5c8a35 45%,#4d6b7a 60%,#3b4a40 100%)"></div>
    <div class="dot dot--green" style="left:30px;top:330px;width:50px;height:50px"></div>
    <div class="dot dot--orange" style="left:68px;top:320px;width:30px;height:30px"></div>
  </article>

  <article class="panel panel--install">
    <div role="img" aria-label="Overhanging green foliage" style="position:absolute;left:0;top:0;width:100%;height:80px;background:linear-gradient(180deg,#4f9a2a 0%,#8cc63f 60%,rgba(140,198,63,0) 100%)"></div>
    <div class="photo" role="img" aria-label="Gardener tending a planted garden bed" style="left:120px;top:-30px;width:140px;height:140px;background:radial-gradient(circle at 50% 50%,#a6cf55 0%,#5f9a33 55%,#2f5e22 100%)"></div>
    <div class="dot dot--blue" style="left:100px;top:70px;width:34px;height:34px"></div>
    <div class="inst-copy">
      <h3 style="margin-top:0">Installation &amp; Construction</h3>
      <p>Upon a well prepared site, The Halvorsen Group are a professional landscape and construction company that works with a whole range of materials and structural designs.</p>
      <p>Browse through our portfolio to see our quality finishes and versatile capabilities including:</p>
      <div class="checks">
        <ul><li>Decking</li><li>Tiling</li><li>Paving</li><li>Pathways</li><li>Walls and Screening</li><li>Irrigation</li><li>Plant supply &amp; Installation</li></ul>
        <ul><li>Lawn</li><li>Water Features</li><li>Rock features</li><li>Lighting</li><li>Concreting</li><li>Aggregate designs</li><li>Metal Sculptures</li></ul>
      </div>
      <h3>Maintenance Programs</h3>
      <p>We understand people can be 'caught up' or procrastinate in attending to landscape maintenance. Once you have invested in an outdoor project, it's important it is retained for continuous enjoyment and longevity, and to avoid any costly neglect!</p>
    </div>
    <div class="photo" role="img" aria-label="Modern two-storey home with landscaped front lawn" style="left:40px;top:420px;width:230px;height:230px;background:linear-gradient(180deg,#bcd8ee 0%,#d8d2c6 35%,#8f8a80 55%,#6fa63f 72%,#4c7f2a 100%)"></div>
    <div class="dot dot--orange" style="left:176px;top:410px;width:46px;height:46px"></div>
  </article>

  <article class="panel panel--consult">
    <div class="photo" role="img" aria-label="Timber house with a landscaped garden and lawn" style="left:40px;top:-40px;width:180px;height:180px;background:linear-gradient(180deg,#d9e7ef 0%,#9a7a5a 45%,#6f5a44 60%,#7fae45 78%,#4d7f2b 100%)"></div>
    <div class="dot dot--green" style="left:30px;top:106px;width:38px;height:38px"></div>
    <div class="consult">
      <h2>Landscape Consulting<br>and <b>Design</b></h2>
      <h3>Construction</h3>
      <ul><li>Bespoke Structural Features</li><li>Water Features</li><li>Paving &amp; Pathways</li><li>Concreting and Aggregate</li></ul>
      <h3>Garden</h3>
      <ul><li>Plant &amp; Tree supply &amp; Installation</li><li>Earth Preparation</li><li>Lawns</li><li>Irrigation Systems</li></ul>
      <h3>Maintenance</h3>
      <ul><li>Garden &amp; Structural</li></ul>
    </div>
    <div class="grass" role="img" aria-label="Fresh green grass with small wildflowers"></div>
  </article>
</section>

</body>
</html>
```